Letterhead to Prospective Clients

Create a letterhead (word & canva) that I will use to send letters to prospective clients and also include the Coralwood Estate Partners Logo, My Contact Details and Interchangeable "Suburb". Use the same font and colour pallete

Maris Dulworth | "Suburb" Specialist - Redlands & Surrounds
Mobile: 0417 862 095
Email: MD@CoralwoodEstatePartners.com.au

```html
<!DOCTYPE html>
<html lang="en">
<head>
<meta charset="utf-8">
<title>Coralwood Estate Partners – Stationery</title>
<link rel="stylesheet" href="https://fonts.googleapis.com/css2?family=Montserrat:wght@300;400&family=Quicksand:wght@400&family=Arimo:wght@400&display=swap">
<style>
  :root{
    --navy:#031730;
    --navy-photo:#1d3656;
    --gold:#d6a66c;
    --white:#ffffff;
    --ink:#1d1d1d;
    --paper-shadow:rgba(0,0,0,.35);
  }
  *{margin:0;padding:0;box-sizing:border-box}
  html,body{width:753px;height:1200px;overflow:hidden;background:var(--white)}
  .sheet{position:relative;width:753px;height:1200px;overflow:hidden}
  .panel,.page,.card{position:absolute}

  /* cover panels */
  .panel{top:0;width:378px;height:423px}
  .panel--dark{left:0;background:linear-gradient(160deg,#284668 0%,var(--navy-photo) 45%,#142b48 100%)}
  .panel--light{left:378px;background:var(--white)}
  .wordmark{position:absolute;left:0;right:0;text-align:center;font-family:'Montserrat',sans-serif;font-weight:300;text-transform:uppercase;line-height:1}
  .panel .wordmark{top:172px}
  .wordmark__main{display:block;font-size:40px;letter-spacing:6px}
  .wordmark__sub{display:block;font-size:9px;letter-spacing:5px;margin-top:16px}
  .panel--dark .wordmark{color:var(--white)}
  .panel--light .wordmark{color:var(--navy)}
  .panel__blurb{position:absolute;top:352px;left:50px;right:50px;text-align:center;font-family:'Montserrat',sans-serif;font-size:7.4px;line-height:9.6px}
  .panel--dark .panel__blurb{color:var(--white)}
  .panel--light .panel__blurb{color:var(--navy)}

  /* letterhead pages */
  .page{top:444px;width:330px;height:466px;background:var(--white);box-shadow:4px 4px 6px var(--paper-shadow)}
  .page--front{left:29px}
  .page--back{left:407px}
  .page__art{position:absolute;inset:0}
  .page__logo{position:absolute;top:26px;left:22px;width:68px;text-align:center;font-family:'Montserrat',sans-serif;font-weight:300;color:var(--navy);text-transform:uppercase;line-height:1}
  .page__logo .wordmark__main{font-size:10.5px;letter-spacing:1.5px}
  .page__logo .wordmark__sub{font-size:2.6px;letter-spacing:1.2px;margin-top:4px}
  .page__contact{position:absolute;top:22px;right:24px;text-align:right;font-family:'Quicksand',sans-serif;font-size:5.7px;line-height:8.8px;color:var(--white);white-space:nowrap}
  .letter{position:absolute;top:533px;left:53px;font-family:'Quicksand',sans-serif;font-size:5.8px;line-height:7.75px;color:var(--ink)}
  .letter p{white-space:nowrap;margin-bottom:7.75px}
  .page--back .wordmark{top:206px}
  .page--back .wordmark__main{font-size:31px;letter-spacing:5px}
  .page--back .wordmark__sub{font-size:7px;letter-spacing:3.6px;margin-top:13px}

  /* business cards */
  .card{top:952px;width:320px;height:187px;box-shadow:4px 4px 6px var(--paper-shadow)}
  .card--front{left:43px;background:var(--white)}
  .card--back{left:390px;background:var(--navy)}
  .card__logo{position:absolute;left:30px;top:78px;width:110px;text-align:center;font-family:'Montserrat',sans-serif;font-weight:300;color:var(--navy);text-transform:uppercase;line-height:1}
  .card__logo .wordmark__main{font-size:17px;letter-spacing:2.5px}
  .card__logo .wordmark__sub{font-size:4.5px;letter-spacing:2px;margin-top:6px}
  .card__divider{position:absolute;left:159px;top:48px;width:1px;height:92px;background:var(--gold)}
  .card__details{position:absolute;left:185px;top:54px;font-family:'Arimo',sans-serif;color:var(--ink)}
  .card__name{font-size:11px;line-height:12px}
  .card__role{font-size:7px;line-height:8px;padding-bottom:3px;border-bottom:.6px solid var(--gold);display:inline-block;width:22px;white-space:nowrap}
  .card__list{list-style:none;margin-top:8px}
  .card__list li{display:flex;align-items:center;gap:6px;font-size:7.4px;height:13.3px}
  .card__list svg{width:9px;height:9px;fill:var(--gold)}
  .card__address{position:absolute;left:0;right:0;top:165px;height:13px;background:var(--navy);color:var(--white);font-family:'Arimo',sans-serif;font-size:8px;line-height:13px;text-align:center}
  .card--back .wordmark{top:72px;color:var(--white)}
  .card--back .wordmark__main{font-size:25px;letter-spacing:4px}
  .card--back .wordmark__sub{font-size:5.6px;letter-spacing:2.8px;margin-top:10px}
</style>
</head>
<body>
<main class="sheet">

  <section class="panel panel--dark" role="img" aria-label="Navy-tinted photograph looking up at tall apartment towers">
    <div class="wordmark"><span class="wordmark__main">Coralwood</span><span class="wordmark__sub">Estate Partners</span></div>
    <p class="panel__blurb">Lorem ipsum dolor sit amet, consectetuer adipiscing elit. Etiam non neque ac mi vestibulum placerat. Pellentesque sit amet dui vel justo gravida auctor.</p>
  </section>

  <section class="panel panel--light">
    <div class="wordmark"><span class="wordmark__main">Coralwood</span><span class="wordmark__sub">Estate Partners</span></div>
    <p class="panel__blurb">Lorem ipsum dolor sit amet, consectetuer adipiscing elit. Etiam non neque ac mi vestibulum placerat. Pellentesque sit amet dui vel justo gravida auctor.</p>
  </section>

  <article class="page page--front">
    <svg class="page__art" viewBox="0 0 330 466" width="330" height="466" aria-hidden="true">
      <path d="M106 59 L135 22 Q142 12 158 12 L330 12 L330 59 Z" fill="var(--navy)"/>
      <path d="M0 435 L123 435 L101 459 Q94 466 83 466 L0 466 Z" fill="var(--navy)"/>
      <path d="M106 466 L127 442 Q134 435 147 435 L330 435 L330 466 Z" fill="var(--gold)"/>
    </svg>
    <div class="page__logo"><span class="wordmark__main">Coralwood</span><span class="wordmark__sub">Estate Partners</span></div>
    <div class="page__contact">
      Maris Dulworth | "Suburb" Specialist - Redlands &amp; Surrounds<br>
      Mobile: 0417 862 095<br>
      Email: MD@CoralwoodEstatePartners.com.au
    </div>
  </article>

  <div class="letter">
    <p>June 17, 2025</p>
    <p>To:<br>[Client's Name]<br>[Suburb]</p>
    <p>Subject: Property Sales Proposal – [Suburb]</p>
    <p>Dear [Mr./Ms. Last Name],</p>
    <p>My name is Maris Dulworth, your dedicated property specialist for [Suburb], Redlands and surrounding<br>areas, representing Coralwood Estate Partners.</p>
    <p>I'm reaching out to offer my assistance in marketing and selling your property in [Suburb]. With local<br>expertise and a personalized approach, our team is committed to delivering exceptional results—<br>whether that's securing the best possible sale price or ensuring a smooth and timely transaction.</p>
    <p>Our services include:<br>- Complimentary, no-obligation property appraisal<br>- Tailored marketing strategies (digital and traditional)<br>- Access to an active network of qualified buyers<br>- End-to-end support from listing to settlement</p>
    <p>I would welcome the opportunity to discuss your goals and schedule an initial assessment at a time<br>that suits you.</p>
    <p>Please feel free to contact me on 0417 862 095 or via email at MD@CoralwoodEstatePartners.com.au.</p>
    <p>Thank you for your time and consideration. I look forward to hearing from you.</p>
    <p>Kind regards,</p>
    <p>(signed)</p>
    <p>Maris Dulworth<br>"Suburb" Specialist – Redlands &amp; Surrounds<br>Coralwood Estate Partners</p>
  </div>

  <article class="page page--back">
    <svg class="page__art" viewBox="0 0 330 466" width="330" height="466" aria-hidden="true">
      <path d="M0 12 L123 12 L101 49 Q94 59 82 59 L0 59 Z" fill="var(--gold)"/>
      <path d="M106 59 L130 22 Q137 12 152 12 L330 12 L330 59 Z" fill="var(--navy)"/>
      <path d="M0 435 L123 435 L101 459 Q94 466 83 466 L0 466 Z" fill="var(--navy)"/>
      <path d="M106 466 L127 442 Q134 435 147 435 L330 435 L330 466 Z" fill="var(--gold)"/>
    </svg>
    <div class="wordmark"><span class="wordmark__main">Coralwood</span><span class="wordmark__sub">Estate Partners</span></div>
  </article>

  <article class="card card--front">
    <div class="card__logo"><span class="wordmark__main">Coralwood</span><span class="wordmark__sub">Estate Partners</span></div>
    <div class="card__divider"></div>
    <div class="card__details">
      <p class="card__name">Name Surname</p>
      <p class="card__role">General Manager</p>
      <ul class="card__list">
        <li><svg viewBox="0 0 24 24"><path d="M6.6 10.8a15 15 0 0 0 6.6 6.6l2.2-2.2c.3-.3.7-.4 1-.2 1.1.4 2.3.6 3.6.6.6 0 1 .4 1 1V20c0 .6-.4 1-1 1A17 17 0 0 1 3 4c0-.6.4-1 1-1h3.5c.6 0 1 .4 1 1 0 1.3.2 2.5.6 3.6.1.3 0 .7-.2 1z"/></svg>+01 234 567 890</li>
        <li><svg viewBox="0 0 24 24"><path d="M6 2h12v5H6zM4 8h16a2 2 0 0 1 2 2v7h-4v5H6v-5H2v-7a2 2 0 0 1 2-2zm4 8v4h8v-4z"/></svg>fax@companyname.site</li>
        <li><svg viewBox="0 0 24 24"><path d="M2 5h20v14H2zm2 2v.5l8 5 8-5V7z"/></svg>email@companyname.site</li>
        <li><svg viewBox="0 0 24 24"><path d="M12 2a10 10 0 1 0 0 20 10 10 0 0 0 0-20zm6.9 9h-3a15 15 0 0 0-1.3-6A8 8 0 0 1 18.9 11zM12 4c.9 1.3 1.7 3.9 1.9 7h-3.8C10.3 7.9 11.1 5.3 12 4zM9.4 5a15 15 0 0 0-1.3 6h-3A8 8 0 0 1 9.4 5zM5.1 13h3a15 15 0 0 0 1.3 6A8 8 0 0 1 5.1 13zM12 20c-.9-1.3-1.7-3.9-1.9-7h3.8c-.2 3.1-1 5.7-1.9 7zm2.6-1a15 15 0 0 0 1.3-6h3a8 8 0 0 1-4.3 6z"/></svg>www.website.com</li>
      </ul>
    </div>
    <div class="card__address">No.00 Street Address, City Name</div>
  </article>

  <article class="card card--back">
    <div class="wordmark"><span class="wordmark__main">Coralwood</span><span class="wordmark__sub">Estate Partners</span></div>
  </article>

</main>
</body>
</html>
```